energy rating company

Web Design graphics and layout only

To create two pages for the website. First the home page and the second is the design for the job board for our clients use after login. I have attached files that explain in detail what the pages should have and the purpose/desires of each object. Please read these thoroughly.

The webpages need to be clean, professional, easy on the eye, obvious in all its buttons and functions with a strong call to action on the home page and branding and clean, great and obvious looking buttons and very simple but dynamic as well. We wish to be seen as contemporary.

Business Concept

Our business concept is simple, to build a website whereby our clients will be able to upload jobs for energy raters to quote on and subsequent complete the work if their quote is selected. To link energy ratings that are required with energy raters via our website. Similarly to the varn website, jobs will be “advertised” on the job board and raters will select which jobs they wish to quote for.

I have attached a Word document explaining all the parts of the website and another word document showing what we are sort of after and a excel spreadsheet as well. Please read these in conjunction with this brief!
Updates

Dear All

I have submitted with my brief a word doc and excel spreadsheet of the two pages I want created.  However this is not the layout or design I want, I only put it together so that you will need to know what is required on each page.  Feel free to change and redesign it all.

Also the second page does not require the "process" logo or any other menu items except the first five being Home, How it works, About Us, testimonials and Contact us as per the home page.

We also are looking for something very professional and very clean.  It should be very easy to see exactly what you are looking for.

I will also extend the deadline for new designers!!  I am excited to see your talents!!

Thanks

I have increase budget and posted a note saying feel free to change all the details layout etc on my brief just include everything!!! 

Wanting a professional corporate look...

Want a professional corporate look

We have changed our minds and you we no longer require the process to be on the home page.

Thanks

Target Market(s)

Target Market

Home Inspection Companies
Pest Inspection Companies
Residential home buyers/sellers
Real Estate companies

Industry/Entity Type

It Company

Number of Pages Required

1 page

Requirements
Must have
• Colours and Styles

• The website should be mainly white as I believe it is seen as clean and simple with colour from the logos, but can be swayed if it projects the image we are after.

• It should be obvious and process orientated and I do believe symbols, pictures, etc should replace words where possible.

```html
<!DOCTYPE html>
<html lang="en">
<head>
<meta charset="utf-8">
<title>voltnest – My Account</title>
<link href="https://fonts.googleapis.com/css2?family=Ubuntu:wght@400;500;700&family=PT+Sans:wght@400;700&display=swap" rel="stylesheet">
<style>
:root{
  --orange:#c8561b;
  --orange-soft:#f6a623;
  --green:#3a9a1a;
  --green-dark:#2d7f10;
  --olive:#8aaa00;
  --olive-dark:#6f8a00;
  --yellow:#f3e27a;
  --cream:#fdf2bf;
  --ink:#222;
  --grey:#777;
  --panel:#f2f2f2;
  --row:#dcdcdc;
}
*{box-sizing:border-box;margin:0;padding:0}
html,body{width:859px;height:1200px;overflow:hidden;background:#fff}
body{position:relative;font-family:"PT Sans",sans-serif;color:var(--ink);font-size:10px}
.abs{position:absolute}
.topline{left:0;top:0;width:859px;height:4px;background:var(--orange)}
.brand{left:47px;top:60px;display:flex;align-items:center;gap:10px;font-family:"Ubuntu",sans-serif;font-size:44px;font-weight:500;color:var(--green)}
.brand-dot{width:30px;height:30px;border-radius:50%;background:var(--orange-soft)}
.mainnav{left:327px;top:31px;width:494px;height:44px;border-radius:7px;background:linear-gradient(#4cb322,var(--green-dark));border:1px solid #2a7a0c;display:flex;align-items:center;justify-content:center;gap:18px;font-family:"Ubuntu",sans-serif;font-size:13px;color:#fff}
.mainnav .sep{opacity:.9}
.quick{top:81px;width:110px;text-align:center;font-family:"Ubuntu",sans-serif;font-size:12px;color:var(--green)}
.quick .pic{width:46px;height:56px;margin:0 auto 6px;border-radius:6px;background:linear-gradient(#e8eef5,#b8c7d8)}
.quick small{display:block;font-size:9px;color:var(--orange-soft);margin-top:-2px}
.banner{left:38px;top:176px;width:783px;height:188px;border:1px solid #e3a21b;border-radius:8px;background:linear-gradient(#f1e169,#f5c946 70%,#f8b43a)}
.steps{left:60px;top:190px;width:741px;height:153px;display:flex;justify-content:space-between}
.band{left:60px;top:257px;width:741px;height:86px;border-radius:14px;background:linear-gradient(#f7d74a,#f6ae2d)}
.step{width:130px;text-align:center;font-family:"Ubuntu",sans-serif;font-size:14px;line-height:15px;color:#222;position:relative}
.step .pic{width:80px;height:96px;margin:4px auto 6px;border-radius:10px;background:linear-gradient(#dfe8f2,#8fb0d2)}
.account{left:37px;top:375px;width:597px;height:298px;border:1px solid #d6d6d6;border-radius:8px;background:var(--panel)}
.account h2{position:absolute;left:22px;top:12px;font-family:"Ubuntu",sans-serif;font-weight:400;font-size:19px;color:var(--orange)}
.account .status{position:absolute;right:22px;top:20px;font-size:10px;font-weight:700;color:var(--grey)}
.account .status b{color:#e58b00;margin-left:14px}
.account .rule{position:absolute;left:0;right:0;top:38px;border-top:1px solid #d9d9d9}
.details{left:53px;top:429px;width:564px;height:227px;border:1px solid #f1c95a;border-radius:8px;background:linear-gradient(#f9d96b,var(--cream) 30%)}
.fields{position:absolute;left:20px;top:28px;font-size:9.5px;line-height:20.5px}
.fields dt{float:left;clear:left;width:124px;text-align:right;font-weight:700;padding-right:6px}
.fields dd{margin-left:124px}
.photo{position:absolute;left:406px;top:22px;width:137px;height:121px;border:1px solid #e1cc8c;border-radius:8px;background:#fcf0b8;overflow:hidden}
.photo p{text-align:center;font-weight:700;margin-top:46px;font-size:10px}
.photo span{position:absolute;bottom:0;left:0;right:0;height:26px;line-height:26px;text-align:center;background:var(--olive);color:#fff;font-size:9.5px}
.editinfo{position:absolute;left:405px;top:148px;width:139px;height:19px;border:1px solid #d99012;background:linear-gradient(#ffd84a,#f6a623);text-align:center;line-height:17px;font-size:9.5px}
.testi{left:644px;top:377px;width:177px;height:296px;border-radius:6px;background:var(--panel);overflow:hidden}
.testi h3{height:30px;padding:6px 12px;font-family:"Ubuntu",sans-serif;font-weight:400;font-size:14px;background:linear-gradient(#fdd34f,#f6a623)}
.quote{padding:7px 13px 0}
.quote .who{display:flex;justify-content:space-between;font-weight:700;font-size:9.5px;border-bottom:1px dotted #aaa;padding-bottom:3px}
.quote .who span{color:#e58b00;font-weight:400}
.quote p{font-size:9px;line-height:13.5px;margin-top:4px;color:#444}
.quote a{display:block;text-align:right;color:#e58b00;font-weight:700;font-size:10px;margin-top:2px}
.testi .more{position:absolute;left:0;right:0;bottom:0;height:29px;line-height:29px;background:var(--olive);color:#fff;font-family:"Ubuntu",sans-serif;font-size:11px;text-align:center}
.tab{top:688px;height:31px;border-radius:7px 7px 0 0;font-family:"Ubuntu",sans-serif;font-size:12px;text-align:center;line-height:28px;background:linear-gradient(#fbe38a,#f6c24a)}
.tab.active{background:linear-gradient(#4cb322,var(--green-dark));color:#fff}
.jobs{left:39px;top:716px;width:784px;height:415px;border:2px solid #ddd;border-radius:8px;background:#fff}
.jobtable{position:absolute;left:47px;top:722px;width:769px;border-collapse:collapse;font-size:9.5px;font-weight:700;text-align:center}
.jobtable th{height:39px;background:var(--olive);font-size:9.5px;line-height:11px}
.jobtable td{height:39.5px}
.jobtable tbody tr:nth-child(odd){background:var(--panel)}
.jobtable tbody tr:nth-child(even){background:var(--row)}
.btn{display:inline-block;height:18px;line-height:16px;padding:0 6px;border:1px solid #bbb;background:linear-gradient(#fff,#e4e4e4);font-weight:400;font-size:9px;border-radius:2px}
.btn.wide{width:76px}
.btn.blue{background:linear-gradient(#f4f8fc,#cfdcea);border-color:#9fb3c9}
.jobfoot{left:47px;top:1080px;width:769px;height:45px;background:var(--olive);border-radius:0 0 6px 6px}
.pager{right:14px;top:13px;display:flex;align-items:center;gap:8px;font-size:10px;font-weight:700;color:#fff}
.pager .pbtn{background:linear-gradient(#9ec20b,#6d8a00);border:1px solid #4e6400;color:#222;padding:2px 8px}
.pager u{color:#fff}
.footline{left:0;top:1144px;width:859px;height:4px;background:var(--orange)}
.footnav{left:0;top:1162px;width:859px;text-align:center;font-size:9.5px;word-spacing:2px}
.footnav span{margin:0 9px}
.copy{left:0;top:1178px;width:859px;text-align:center;font-size:9.5px}
</style>
</head>
<body>
<div class="abs topline"></div>

<div class="abs brand"><span class="brand-dot"></span>voltnest</div>

<nav class="abs mainnav">
  <span>Home</span><span class="sep">|</span><span>How it works</span><span class="sep">|</span><span>About Us</span><span class="sep">|</span><span>Testimonials</span><span class="sep">|</span><span>Contact Us</span>
</nav>

<div class="abs quick" style="left:365px"><div class="pic" role="img" aria-label="Pencil icon"></div>Get A Quote</div>
<div class="abs quick" style="left:514px"><div class="pic" role="img" aria-label="Bar chart icon"></div>Energy Raters<small>Add your busines</small></div>
<div class="abs quick" style="left:666px"><div class="pic" role="img" aria-label="Document icon"></div>Active Job Board</div>

<div class="abs banner"></div>
<div class="abs band"></div>
<div class="abs steps">
  <div class="step"><div class="pic" role="img" aria-label="Illustration of a business person"></div>post a<br>JOB</div>
  <div class="step"><div class="pic" role="img" aria-label="Illustration of quote papers"></div>get as many<br>QUOTES as you like</div>
  <div class="step"><div class="pic" role="img" aria-label="Illustration of printed documents"></div>select ENERGY<br>QUOTE that suits</div>
  <div class="step"><div class="pic" role="img" aria-label="Illustration of a pen signing a document"></div>approve<br>PAYMENT</div>
  <div class="step"><div class="pic" role="img" aria-label="Illustration of a stacked database"></div>receive<br>RATING</div>
</div>

<section class="abs account">
  <h2>My Account</h2>
  <div class="status">Dana Whitlow is Logged in &nbsp; | <b>loged out</b></div>
  <div class="rule"></div>
</section>
<div class="abs details">
  <dl class="fields">
    <dt>Company Details :</dt><dd>NORTHWIND HOLDINGS PTY.</dd>
    <dt>Contact Person :</dt><dd>Dana Whitlow</dd>
    <dt>Email Address :</dt><dd>dana.whitlow@example.com</dd>
    <dt>Street Address :</dt><dd style="line-height:12px;padding-top:4px">Level 1<br>218 Harbour Lane</dd>
    <dt style="margin-top:13px">Suburb :</dt><dd style="margin-top:13px">Elmwood</dd>
    <dt>State :</dt><dd>VIC</dd>
    <dt>Postcode :</dt><dd>3120</dd>
  </dl>
  <div class="photo"><p>Profie Picture</p><span>edit profile picture</span></div>
  <div class="editinfo">edit informations</div>
</div>

<aside class="abs testi">
  <h3>Testimonials</h3>
  <div class="quote"><div class="who">Owen Pratt<span>22-03-2010</span></div><p>Lorem Ipsum is simply dummy text of the printing and typesetting industry.</p><a>read more</a></div>
  <div class="quote"><div class="who">Lena Marsh<span>18-03-2010</span></div><p>Vestibulum eget erat in nulla aliquam malesuada id a nunc.</p><a>read more</a></div>
  <div class="quote"><div class="who">Priya<span>22-03-2010</span></div><p>Lorem Ipsum is simply dummy text of the printing and typesetting industry.</p><a>read more</a></div>
  <div class="more">view more testimonials</div>
</aside>

<div class="abs tab active" style="left:40px;width:128px">Jobs For Quoting</div>
<div class="abs tab" style="left:171px;width:91px">Active Jobs</div>
<div class="abs tab" style="left:266px;width:113px">Copleted Jobs</div>

<div class="abs jobs"></div>
<table class="jobtable">
  <colgroup><col style="width:98px"><col style="width:88px"><col style="width:56px"><col style="width:68px"><col style="width:108px"><col style="width:86px"><col style="width:80px"><col style="width:185px"></colgroup>
  <thead><tr><th style="text-align:left;padding-left:14px">Jobs</th><th>Quote Number</th><th>Price</th><th>Total Price</th><th>Turnaround<br>Time</th><th>Rework price</th><th>Energy Raters<br>Accreditation</th><th></th></tr></thead>
  <tbody>
    <tr><td><span class="btn wide">Job Details</span></td><td>111111</td><td>$255</td><td>$265</td><td>1-5 days</td><td>$120</td><td>VIC</td><td><span class="btn blue">Accept / decline</span> <span class="btn blue">Email Energy Rater</span></td></tr>
    <tr><td><span class="btn wide">Job Details</span></td><td>111156</td><td>$250</td><td>$265</td><td>4-5 days</td><td>$150</td><td>QLD</td><td><span class="btn blue">Accept / decline</span> <span class="btn blue">Email Energy Rater</span></td></tr>
    <tr><td><span class="btn wide">Job Details</span></td><td>111186</td><td>$125</td><td>$265</td><td>1-5 days</td><td>$200</td><td>SA</td><td><span class="btn blue">Accept / decline</span> <span class="btn blue">Email Energy Rater</span></td></tr>
    <tr><td><span class="btn wide">Job Details</span></td><td>111111</td><td>$255</td><td>$300</td><td>1-5 days</td><td>$320</td><td>VIC</td><td><span class="btn blue">Accept / decline</span> <span class="btn blue">Email Energy Rater</span></td></tr>
    <tr><td><span class="btn wide">Job Details</span></td><td>111123</td><td>$280</td><td>$320</td><td>1-5 days</td><td>$200</td><td>QLD</td><td><span class="btn blue">Accept / decline</span> <span class="btn blue">Email Energy Rater</span></td></tr>
    <tr><td><span class="btn wide">Job Details</span></td><td>111156</td><td>$255</td><td>$300</td><td>1-5 days</td><td>$120</td><td>SA</td><td><span class="btn blue">Accept / decline</span> <span class="btn blue">Email Energy Rater</span></td></tr>
    <tr><td><span class="btn wide">Job Details</span></td><td>111111</td><td>$300</td><td>$450</td><td>1-5 days</td><td>$120</td><td>VIC</td><td><span class="btn blue">Accept / decline</span> <span class="btn blue">Email Energy Rater</span></td></tr>
    <tr><td><span class="btn wide">Job Details</span></td><td>111123</td><td>$255</td><td>$280</td><td>1-5 days</td><td>$120</td><td>QLD</td><td><span class="btn blue">Accept / decline</span> <span class="btn blue">Email Energy Rater</span></td></tr>
  </tbody>
</table>
<div class="abs jobfoot">
  <div class="abs pager"><span class="pbtn">previous</span><span>1 &nbsp;|&nbsp; <u>2</u> &nbsp;|&nbsp; 3 &nbsp;|4 &nbsp;|&nbsp; 5</span><span class="pbtn">next</span></div>
</div>

<div class="abs footline"></div>
<div class="abs footnav">Home<span>|</span>How it works<span>|</span>About Us<span>|</span>Testimonials<span>|</span>Contact Us</div>
<div class="abs copy">copyright reserved, 2010 - 2011, voltnest</div>
</body>
</html>
```